Flat Belly Design Graphics for Social

I want to create 9 social media graphics (new Instagram size 4:5 (1080 x 1350 pixels) focusing on our Flat Belly Graphics, using the pics attached. Use the attached pics, NO RANDOM STOCK PHOTOGRAPHY. For the color scheme of the graphics, the color palette is attached. YOU MUST POST ALL 9 GRAPHICS IN ONE ENTRY.
Using the 3 titles below, create one set of graphics. 1) with all text, then for the others, use the pictures as detailed below in IMPORTANT:
1. 21-Night Lean Middle Reboot Beyond 50
2. The 20-Second Trim-Core Menu Guide
3. Starlet Tricks to a Slender Midline Beyond 50 - Zero Scalpel Needed
IMPORTANT:
Only use RK Pic 1 and RK Pic 2 with the title, 21-Night Lean Middle Reboot Beyond 50
Only use meal plan1 and meal plan2 pics with the title, 20-Second Trim-Core Menu Guide
Only use starlet tricks 1 and starlet tricks 2 pics with the title, Starlet Tricks to a Slender Midline Beyond 50 - Zero Scalpel Needed
women over 40

```html
<!DOCTYPE html>
<html lang="en">
<head>
<meta charset="utf-8">
<title>21-Night Lean Middle Reboot — Social Set</title>
<link href="https://fonts.googleapis.com/css2?family=Bebas+Neue&family=Anton&display=swap" rel="stylesheet">
<style>
  :root{
    --board:#f6d8dc;
    --forest:#2f504b;
    --forest-deep:#274540;
    --teal:#5a9189;
    --rose:#e29bb2;
    --rose-deep:#c9708e;
    --blush:#f7dfe4;
    --blush-light:#fbeef0;
    --white:#ffffff;
    --skin:#c9a08a;
    --knit:#ece9e6;
  }
  *{box-sizing:border-box;margin:0;padding:0}
  html,body{width:1200px;height:853px;overflow:hidden;background:var(--board)}
  .board{position:relative;width:1200px;height:853px}
  .card{position:absolute;overflow:hidden;box-shadow:0 10px 14px -8px rgba(80,40,50,.35)}
  .card-hero{left:88px;top:161px;width:404px;height:504px}
  .c1{left:550px}.c2{left:753px}.c3{left:959px}
  .r1{top:55px}.r2{top:312px}.r3{top:562px}
  .tile{width:186px;height:233px}
  .bebas{font-family:'Bebas Neue',sans-serif;line-height:.9}
  .anton{font-family:'Anton',sans-serif;line-height:.95;letter-spacing:-.2px}
  .abs{position:absolute;z-index:2}
  .ring{position:absolute;z-index:2;border-radius:50%;background:var(--forest)}
  .badge-box{position:absolute;z-index:2;border:1px solid var(--white);color:var(--white);text-align:center}
  .backdrop{position:absolute;z-index:0;left:0;top:0}
  .photo{position:absolute;z-index:1}
  .bg-forest{background:radial-gradient(circle at 20% 40%,#5a8d85 0%,var(--forest) 55%,var(--forest-deep) 100%)}
  .bg-forest-flat{background:var(--forest)}
  .bg-rose{background:linear-gradient(180deg,var(--blush) 0%,var(--rose) 100%)}
  .bg-blush{background:linear-gradient(180deg,var(--blush-light),var(--blush))}
  .photo-person{background:linear-gradient(180deg,#3a2c28 0%,var(--skin) 24%,var(--knit) 44%,#e4dad4 70%,#2a2526 100%);border-radius:46% 46% 8px 8px / 20% 20% 8px 8px;opacity:.95}
  .photo-food{background:radial-gradient(circle at 40% 45%,#c94a55 0%,#8a5a6a 40%,#5a3d2c 100%)}
  .photo-table{background:linear-gradient(135deg,#e2c3ad 0%,#a98a63 40%,#6a4a35 70%,#7d8a45 100%)}
  .photo-spread{background:linear-gradient(90deg,#d9623e 0%,#c99a44 30%,#5a4030 50%,#8aa048 75%,#cf4a44 100%)}
  .photo-friends{background:linear-gradient(180deg,#8c6a5a 0%,#d7b7a2 35%,#e8d8cf 65%,#8fa6c0 100%);border-radius:46% 46% 0 0 / 22% 22% 0 0}
  .photo-friends-wide{background:linear-gradient(180deg,#6a4c40 0%,#c49a82 50%,#f3e6e8 100%)}
  .tag{background:var(--forest);color:var(--blush-light);padding:1px 3px;line-height:.95}
  .t-white{color:var(--white)}.t-forest{color:var(--forest)}
  .center{text-align:center}
  .outlined{text-shadow:-1px -1px 0 var(--forest),1px -1px 0 var(--forest),-1px 1px 0 var(--forest),1px 1px 0 var(--forest)}
</style>
</head>
<body>
<main class="board">

  <section class="card card-hero bg-forest">
    <div class="photo photo-person" role="img" aria-label="Smiling woman in a white cropped sweater pointing at her midsection" style="left:62px;top:172px;width:200px;height:332px"></div>
    <svg class="abs" style="left:0;bottom:0" width="404" height="130" viewBox="0 0 404 130" aria-hidden="true">
      <path d="M0 70 C60 110 140 120 230 80 C300 50 360 30 404 40 L404 48 C360 42 300 62 230 95 C140 135 60 120 0 85Z" fill="var(--teal)"/>
      <path d="M0 85 C60 120 140 135 230 95 C300 62 360 42 404 48 L404 130 L0 130Z" fill="var(--forest-deep)"/>
    </svg>
    <div class="abs bebas t-white center" style="left:0;right:0;top:28px;font-size:74px">21-NIGHT</div>
    <div class="abs bebas t-white center" style="left:0;right:0;top:100px;font-size:52px">LEAN MIDDLE REBOOT</div>
    <div class="ring" style="left:262px;top:166px;width:136px;height:136px"></div>
    <div class="abs bebas t-white center" style="left:262px;top:196px;width:136px;font-size:38px">BEYOND<br><span style="font-size:50px">50</span></div>
    <div class="ring" style="left:300px;top:310px;width:34px;height:34px"></div>
    <div class="ring" style="left:334px;top:339px;width:13px;height:13px"></div>
  </section>

  <section class="card tile c1 r1 bg-forest">
    <div class="photo photo-person" role="img" aria-label="Smiling woman in a white cropped sweater pointing at her midsection" style="left:30px;top:80px;width:82px;height:153px"></div>
    <svg class="abs" style="left:0;bottom:0" width="186" height="60" viewBox="0 0 186 60" aria-hidden="true">
      <path d="M0 20 C40 55 90 40 186 10 L186 18 C90 48 40 62 0 30Z" fill="var(--teal)"/>
      <path d="M0 30 C40 62 90 48 186 18 L186 60 L0 60Z" fill="var(--forest-deep)"/>
    </svg>
    <div class="abs bebas t-white center" style="left:0;right:0;top:12px;font-size:34px">21-NIGHT</div>
    <div class="abs bebas t-white center" style="left:0;right:0;top:46px;font-size:25px">LEAN MIDDLE REBOOT</div>
    <div class="ring" style="left:116px;top:80px;width:62px;height:62px"></div>
    <div class="abs bebas t-white center" style="left:116px;top:93px;width:62px;font-size:17px">BEYOND<br><span style="font-size:24px">50</span></div>
    <div class="ring" style="left:140px;top:146px;width:14px;height:14px"></div>
    <div class="ring" style="left:156px;top:160px;width:6px;height:6px"></div>
  </section>

  <section class="card tile c2 r1 bg-forest-flat">
    <svg class="backdrop" width="186" height="233" viewBox="0 0 186 233" aria-hidden="true">
      <path d="M84 0 L186 0 L186 233 L80 233 C100 180 90 120 120 80 C140 50 100 20 84 0Z" fill="var(--rose)"/>
    </svg>
    <div class="photo photo-person" role="img" aria-label="Smiling woman in a white cropped sweater pointing at her midsection" style="left:80px;top:82px;width:98px;height:151px"></div>
    <div class="abs anton t-white" style="left:13px;top:14px;font-size:27px">21-NIGHT LEAN<br>MIDDLE REBOOT</div>
    <div class="abs bebas t-white" style="left:13px;top:84px;font-size:30px">BEYOND<br>50</div>
    <div class="ring" style="left:140px;top:112px;width:14px;height:14px"></div>
    <div class="ring" style="left:157px;top:112px;width:6px;height:6px"></div>
    <div class="ring" style="left:60px;top:196px;width:18px;height:18px;background:var(--blush)"></div>
    <div class="ring" style="left:52px;top:186px;width:7px;height:7px;background:var(--blush)"></div>
  </section>

  <section class="card tile c3 r1 bg-forest-flat">
    <svg class="backdrop" width="186" height="233" viewBox="0 0 186 233" aria-hidden="true">
      <path d="M0 0 L186 0 L186 20 C150 60 140 80 120 85 C80 95 40 130 0 105Z" fill="var(--blush)"/>
    </svg>
    <div class="photo photo-person" role="img" aria-label="Smiling woman in a white cropped sweater pointing at her midsection" style="left:78px;top:82px;width:104px;height:151px"></div>
    <div class="abs anton t-forest" style="left:14px;top:12px;font-size:34px">21-NIGHT</div>
    <div class="abs anton t-forest" style="left:18px;top:54px;font-size:19px">LEAN MIDDLE<br>REBOOT</div>
    <div class="ring" style="left:152px;top:50px;width:14px;height:14px;background:var(--rose)"></div>
    <div class="ring" style="left:142px;top:68px;width:7px;height:7px;background:var(--rose)"></div>
    <div class="badge-box bebas" style="left:18px;top:124px;width:46px;height:50px;padding-top:4px;font-size:14px">BEYOND<br><span style="font-size:26px">50</span></div>
  </section>

  <section class="card tile c1 r2 bg-rose">
    <div class="photo photo-table" role="img" aria-label="Healthy foods on a wooden table" style="left:100px;top:132px;width:86px;height:86px"></div>
    <div class="photo photo-food" role="img" aria-label="Bowl of mixed berries and grapes" style="left:12px;top:90px;width:126px;height:126px;border-radius:50%;border:2px solid var(--white);z-index:2"></div>
    <svg class="abs" style="left:0;bottom:0;z-index:1" width="186" height="40" viewBox="0 0 186 40" aria-hidden="true">
      <path d="M0 25 C60 10 120 40 186 15 L186 40 L0 40Z" fill="var(--rose-deep)"/>
    </svg>
    <div class="abs bebas t-forest" style="left:15px;top:12px;font-size:30px">THE 20-SECOND</div>
    <div class="abs bebas t-forest" style="left:17px;top:42px;font-size:30px">TRIM-CORE</div>
    <div class="ring" style="left:116px;top:64px;width:64px;height:64px;background:var(--rose-deep);z-index:3"></div>
    <div class="abs bebas t-white center" style="left:116px;top:78px;width:64px;font-size:19px;z-index:4">MENU<br>GUIDE</div>
    <div class="ring" style="left:152px;top:134px;width:14px;height:14px;background:var(--rose-deep);z-index:3"></div>
    <div class="ring" style="left:165px;top:150px;width:6px;height:6px;background:var(--rose-deep);z-index:3"></div>
  </section>

  <section class="card tile c2 r2 bg-blush">
    <div class="photo photo-table" role="img" aria-label="Chicken, berries, vegetables and a meal planner on a wooden table" style="left:0;top:108px;width:186px;height:125px"></div>
    <div class="abs bebas t-forest" style="left:15px;top:10px;font-size:31px">THE 20-SECOND</div>
    <div class="abs bebas t-forest" style="left:15px;top:42px;font-size:26px">TRIM-CORE</div>
    <div class="abs bebas tag" style="left:122px;top:42px;font-size:22px">MENU<br>GUIDE</div>
    <div class="ring" style="left:96px;top:78px;width:14px;height:14px"></div>
    <div class="ring" style="left:88px;top:84px;width:6px;height:6px"></div>
  </section>

  <section class="card tile c3 r2 bg-blush">
    <div class="photo photo-spread" role="img" aria-label="Fresh produce and fish framing a meal planner notebook" style="left:0;top:0;width:186px;height:120px"></div>
    <div class="abs bebas t-forest center" style="left:0;right:0;top:128px;font-size:30px">THE 20-SECOND</div>
    <div class="abs bg-forest-flat" style="left:0;top:178px;width:186px;height:55px;z-index:1"></div>
    <div class="abs anton t-white outlined" style="left:56px;top:162px;font-size:22px">TRIM-CORE</div>
    <div class="ring" style="left:40px;top:198px;width:14px;height:14px;background:var(--white)"></div>
    <div class="ring" style="left:32px;top:200px;width:5px;height:5px;background:var(--white)"></div>
    <div class="abs bebas t-white" style="left:66px;top:196px;font-size:26px">MENU GUIDE</div>
  </section>

  <section class="card tile c1 r3 bg-blush">
    <svg class="backdrop" width="186" height="233" viewBox="0 0 186 233" aria-hidden="true">
      <path d="M186 40 C150 60 140 120 130 233 L186 233Z" fill="var(--rose)"/>
    </svg>
    <div class="photo photo-friends" role="img" aria-label="Two women sharing a whispered secret, one looking surprised" style="left:90px;top:94px;width:96px;height:139px"></div>
    <div class="abs anton t-forest" style="left:16px;top:12px;font-size:19px">STARLET TRICKS<br>TO A SLENDER<br>MIDLINE</div>
    <div class="abs anton t-forest" style="left:16px;top:74px;font-size:20px">BEYOND 50</div>
    <div class="abs bebas tag" style="left:16px;top:100px;font-size:16px">ZERO SCALPEL<br>NEEDED</div>
    <div class="ring" style="left:62px;top:138px;width:14px;height:14px"></div>
    <div class="ring" style="left:52px;top:144px;width:6px;height:6px"></div>
  </section>

  <section class="card tile c2 r3 bg-blush">
    <div class="photo photo-friends-wide" role="img" aria-label="Woman whispering to a delighted friend" style="left:0;top:0;width:186px;height:124px"></div>
    <div class="abs anton t-forest" style="left:15px;top:144px;font-size:18px">STARLET TRICKS TO A<br>SLENDER MIDLINE</div>
    <div class="ring" style="left:152px;top:171px;width:12px;height:12px"></div>
    <div class="ring" style="left:167px;top:176px;width:5px;height:5px"></div>
    <div class="abs anton t-forest" style="left:15px;top:190px;font-size:22px">BEYOND 50</div>
    <div class="abs bebas tag" style="left:107px;top:194px;font-size:11px;padding:1px 2px">ZERO SCALPEL<br>NEEDED</div>
  </section>

  <section class="card tile c3 r3" style="background:linear-gradient(180deg,var(--blush-light),var(--rose))">
    <div class="photo photo-friends" role="img" aria-label="Two women sharing a whispered secret, one looking surprised" style="left:40px;top:94px;width:108px;height:139px"></div>
    <div class="abs bebas t-forest center" style="left:0;right:0;top:14px;font-size:23px">STARLET TRICKS</div>
    <div class="abs bebas t-forest center" style="left:0;right:0;top:34px;font-size:19px">TO A SLENDER MIDLINE</div>
    <div class="abs anton t-forest" style="left:24px;top:54px;font-size:22px">BEYOND 50</div>
    <div class="abs bebas tag" style="left:118px;top:57px;font-size:11px;padding:1px 2px">ZERO SCALPEL<br>NEEDED</div>
    <div class="ring" style="left:26px;top:104px;width:8px;height:8px"></div>
    <div class="ring" style="left:34px;top:112px;width:13px;height:13px"></div>
    <div class="ring" style="left:164px;top:146px;width:10px;height:10px"></div>
    <div class="ring" style="left:154px;top:160px;width:16px;height:16px"></div>
  </section>

</main>
</body>
</html>
```